Verpackungen für ein Standbodenbeutel Doypack
Zielgruppe
Wir betreiben eine eigene Öl-Manufaktur und bieten ausschließlich natureine Speiseöle und Tierprodukte - Superfood pulver.
Aufgabenstellung
Es wird auf einen Standbodenbeutel Doypack (braun) gedruckt. Es handelt sich um das Produkt Bio Hagebuttenpulver
Es sollte Naturel aussehen , was auf dem Packung stehen sollte u.a.
Schonend gemahlen
100% Vegan
100% natürlich
Ohne Zusatzstoffe
Verzehrempfehlung : Täglich 2 Teelöffel Bio Hagebuttenpulver nach Wunsch einnehmen.
Nährwert Tabelle
Eine Vorlage wurde vom Standbeutel wurde hochgeladen, auch das Firmen Logo wurde hochgeladen.
Die Datei sollteals Adobe Ai und ID
Bei Rückfragen einfach anschfreiben.

```html
<!DOCTYPE html>
<html lang="de">
<head>
<meta charset="utf-8">
<title>Bio Hagebutte Pulver – Standbodenbeutel</title>
<link href="https://fonts.googleapis.com/css2?family=Josefin+Sans:wght@300;600&family=Ms+Madi&display=swap" rel="stylesheet">
<style>
  :root {
    --kraft: #c9a57c;
    --kraft-light: #d4b38c;
    --kraft-dark: #bf9a70;
    --rosehip-red: #b72a15;
    --ink: #1c1a18;
    --brand-teal: #1a9bb0;
  }
  html, body {
    margin: 0;
    padding: 0;
    overflow: hidden;
  }
  .pouch {
    position: relative;
    width: 862px;
    height: 1200px;
    overflow: hidden;
    background: var(--kraft);
  }
  .floral-pattern {
    position: absolute;
    inset: 0;
    background: radial-gradient(ellipse at 50% 45%, var(--kraft-light) 0%, var(--kraft) 60%, var(--kraft-dark) 100%);
  }
  .zip-seal {
    position: absolute;
    left: 0;
    right: 0;
    top: 180px;
    height: 14px;
    border-top: 2px solid rgba(255, 255, 255, 0.25);
    border-bottom: 2px solid rgba(120, 90, 60, 0.25);
  }
  .label-disc {
    position: absolute;
    left: 440px;
    top: 555px;
    width: 470px;
    height: 470px;
    margin: -235px 0 0 -235px;
    border-radius: 50%;
    background: var(--rosehip-red);
    box-shadow: 0 0 0 3px var(--kraft), 0 0 0 6px var(--ink);
  }
  .brand-dot {
    position: absolute;
    left: 424px;
    top: 380px;
    width: 30px;
    height: 30px;
    border-radius: 50%;
    background: var(--brand-teal);
  }
  .brand-name {
    position: absolute;
    left: 0;
    width: 862px;
    top: 420px;
    text-align: center;
    font-family: "Josefin Sans", sans-serif;
    font-weight: 600;
    font-size: 27px;
    letter-spacing: 1px;
    color: var(--brand-teal);
  }
  .product-name {
    position: absolute;
    z-index: 1;
    left: 0;
    width: 862px;
    top: 448px;
    margin: 0;
    text-align: center;
    font-family: "Ms Madi", cursive;
    font-weight: 400;
    font-size: 190px;
    line-height: 1;
    color: var(--ink);
  }
  .product-qualifier {
    position: absolute;
    z-index: 2;
    font-family: "Josefin Sans", sans-serif;
    font-weight: 300;
    color: var(--ink);
    letter-spacing: 7px;
    font-size: 26px;
    line-height: 1;
  }
  .product-qualifier.bio { left: 366px; top: 480px; }
  .product-qualifier.pulver { left: 398px; top: 618px; }
  .seal-row {
    position: absolute;
    top: 812px;
    left: 222px;
    display: flex;
    gap: 28px;
  }
  .seal {
    width: 88px;
    height: 88px;
    border-radius: 50%;
    border: 3px solid var(--ink);
    box-sizing: border-box;
  }
  .seal.solid { background: var(--ink); }
</style>
</head>
<body>
  <main class="pouch">
    <div class="floral-pattern" role="img" aria-label="Feine Linienzeichnung von Hagebuttenzweigen mit Blättern und Früchten als Hintergrundmuster"></div>
    <div class="zip-seal"></div>

    <div class="label-disc"></div>

    <div class="brand-dot"></div>
    <div class="brand-name">Kernhain</div>

    <div class="product-qualifier bio">BIO</div>
    <h1 class="product-name">Hagebutte</h1>
    <div class="product-qualifier pulver">PULVER</div>

    <div class="seal-row" aria-label="Qualitätssiegel">
      <div class="seal"></div>
      <div class="seal solid"></div>
      <div class="seal"></div>
      <div class="seal"></div>
    </div>
  </main>
</body>
</html>
```